Design a Professional Business Card for Velmora Arcs

Design a business card for Velmora Arcs, we are a National Sport Court Company.

West Region Address: 4175 Quill Harbor Ln, Suite #215 Corrigan Springs, Montana 80467
East Region Address: 3817 Tamsin Rd E, Halloway Bay, Georgia 34583

Target Market(s)

High End Residential & Institutional Clients

Industry/Entity Type

Design & Construction

Contact Information for Business Card

Logo/Brand/Colors/ name, number (provided in comments)

Requirements
Must have
• Colors only provided in logo
Should not have
• Any other colors not in existing logo (attached)

```html
<!DOCTYPE html>
<html lang="en">
<head>
<meta charset="utf-8">
<title>Velmora Arcs — Business Card</title>
<link href="https://fonts.googleapis.com/css2?family=Montserrat:wght@400;500;700&display=swap" rel="stylesheet">
<style>
  :root {
    --navy: #1c3667;
    --green: #126936;
    --white: #ffffff;
    --page: #e9e9e9;
    --faint: #eef0f4;
  }
  * { margin: 0; padding: 0; box-sizing: border-box; }
  html, body {
    width: 1200px;
    height: 1200px;
    overflow: hidden;
    background: var(--page);
    font-family: "Montserrat", Arial, sans-serif;
  }
  .card {
    position: absolute;
    left: 164px;
    width: 871px;
    height: 510px;
    background: var(--white);
    overflow: hidden;
  }
  .card--front { top: 66px; }
  .card--back { top: 630px; }

  .accent-circle {
    position: absolute;
    border-radius: 50%;
  }
  .card--front .accent-circle {
    left: 342px;
    top: -185px;
    width: 476px;
    height: 476px;
    background: var(--green);
  }
  .card--back .accent-circle {
    left: 473px;
    top: 105px;
    width: 480px;
    height: 480px;
    background: var(--faint);
  }

  .contact {
    position: absolute;
    left: 52px;
    top: 284px;
    color: var(--navy);
    font-size: 19px;
    line-height: 24px;
  }
  .contact__row {
    display: flex;
    align-items: flex-start;
    gap: 12px;
    margin-bottom: 10px;
  }
  .contact__row--address { margin-top: 24px; }
  .contact__icon {
    width: 20px;
    height: 24px;
    flex: none;
    fill: var(--navy);
  }
  .region-label {
    color: var(--green);
    font-weight: 700;
  }

  .brand {
    position: absolute;
    left: 84px;
    top: 95px;
    display: flex;
    align-items: center;
    gap: 18px;
  }
  .brand__dot {
    width: 90px;
    height: 90px;
    border-radius: 50%;
    background: var(--green);
  }
  .brand__name {
    color: var(--navy);
    font-weight: 700;
    font-size: 38px;
    line-height: 40px;
    letter-spacing: 4px;
    text-transform: uppercase;
  }
</style>
</head>
<body>

<section class="card card--front" aria-label="Business card front">
  <div class="accent-circle"></div>

  <div class="contact">
    <div class="contact__row">
      <svg class="contact__icon" viewBox="0 0 24 24" aria-hidden="true"><path d="M6.6 10.8a15.1 15.1 0 0 0 6.6 6.6l2.2-2.2a1 1 0 0 1 1-.25 11.4 11.4 0 0 0 3.6.57 1 1 0 0 1 1 1V20a1 1 0 0 1-1 1A17 17 0 0 1 3 4a1 1 0 0 1 1-1h3.5a1 1 0 0 1 1 1c0 1.25.2 2.45.57 3.57a1 1 0 0 1-.25 1z"/></svg>
      <span>1234 567 890</span>
    </div>
    <div class="contact__row">
      <svg class="contact__icon" viewBox="0 0 24 24" aria-hidden="true"><path d="M3 5h18a1 1 0 0 1 1 1v12a1 1 0 0 1-1 1H3a1 1 0 0 1-1-1V6a1 1 0 0 1 1-1zm9 7.2L20 7.5V7H4v.5z"/></svg>
      <span>info@velmoraarcs.com</span>
    </div>
    <div class="contact__row contact__row--address">
      <svg class="contact__icon" viewBox="0 0 24 24" aria-hidden="true"><path d="M12 2a7 7 0 0 1 7 7c0 5-7 13-7 13S5 14 5 9a7 7 0 0 1 7-7zm0 4.5a2.5 2.5 0 1 0 0 5 2.5 2.5 0 0 0 0-5z"/></svg>
      <div>
        <div class="region-label">West Region:</div>
        <div>4175 Quill Harbor Ln, Suite #215 Corrigan Springs, Montana 80467</div>
        <div class="region-label">East Region:</div>
        <div>3817 Tamsin Rd E, Halloway Bay, Georgia 34583</div>
      </div>
    </div>
  </div>
</section>

<section class="card card--back" aria-label="Business card back">
  <div class="accent-circle"></div>
  <div class="brand">
    <div class="brand__dot"></div>
    <div class="brand__name">Velmora<br>Arcs</div>
  </div>
</section>

</body>
</html>
```